Business incubator; Angel investments; Consulting for startups

We need new office equipment

Target Market(s)

Start up Company

Font styles to use
Sans Serif

Colors

Designer to choose only greyscale colors for use in the design.

Requirements
Must have
• Existing company logo
Nice to have
• Corporate according to the website www.twm-norvane.com
Should not have
• Colors off gray

```html
<!DOCTYPE html>
<html lang="en">
<head>
<meta charset="utf-8">
<title>TWM Norvane Letterhead</title>
<link href="https://fonts.googleapis.com/css2?family=Montserrat:ital,wght@0,400;0,600;0,700;1,400&display=swap" rel="stylesheet">
<style>
  :root {
    --canvas: #e4e4e4;
    --paper: #ffffff;
    --ink: #111111;
    --body-ink: #1e1e1e;
    --bar-light: #b5b5b5;
    --bar-dark: #808080;
    --mark: #6e6e6e;
    --band-1: #7b7b7b;
    --band-2: #919191;
    --band-3: #c9c9c9;
    --band-4: #e6e6e6;
    --band-text-light: #ffffff;
    --band-text-3: #8c8c8c;
    --band-text-4: #9a9a9a;
    --sign-fill: #ececec;
  }
  * { margin: 0; padding: 0; box-sizing: border-box; }
  html, body {
    width: 1200px; height: 900px; overflow: hidden;
    background: var(--canvas);
    font-family: "Montserrat", sans-serif;
  }
  .letterhead {
    position: absolute; left: 268px; top: 20px;
    width: 664px; height: 860px;
    background: var(--paper);
    box-shadow: 0 4px 14px rgba(0,0,0,0.18);
    overflow: hidden;
  }
  .side-bar { position: absolute; left: 0; top: 0; width: 13px; height: 783px; background: var(--bar-dark); }
  .side-bar::before { content: ""; position: absolute; left: 0; top: 0; width: 13px; height: 138px; background: var(--bar-light); }

  .brand { position: absolute; left: 28px; top: 26px; display: flex; align-items: center; gap: 10px; }
  .brand-square { width: 87px; height: 87px; border-radius: 5px; background: var(--mark); }
  .brand-name { font-weight: 600; font-size: 18px; color: var(--mark); letter-spacing: 0.02em; }

  .letter-date { position: absolute; right: 116px; top: 188px; font-weight: 700; font-size: 12.4px; color: var(--ink); }

  .letter-body { position: absolute; left: 137px; top: 243px; width: 412px; font-size: 11.3px; line-height: 18.2px; color: var(--body-ink); }
  .recipient { margin-bottom: 15px; }
  .recipient-name { font-weight: 700; font-size: 12.2px; color: var(--ink); }
  .recipient-role { font-style: italic; }
  .letter-body p { margin-bottom: 15px; }

  .sign-off { position: absolute; right: 116px; top: 623px; width: 160px; text-align: right; font-size: 11.7px; color: var(--body-ink); }
  .signature { position: absolute; left: 445px; top: 645px; width: 111px; height: 34px; background: linear-gradient(90deg, var(--sign-fill), #f6f6f6); border-radius: 4px; }
  .sender-name { position: absolute; left: 430px; width: 144px; top: 682px; text-align: center; font-weight: 700; font-size: 12.4px; color: var(--ink); }

  .contact-band { position: absolute; left: 0; top: 783px; width: 664px; height: 77px; }
  .contact-band svg { position: absolute; left: 0; top: 0; }
  .contact-item { position: absolute; top: 0; height: 77px; display: flex; flex-direction: column; align-items: center; justify-content: center; gap: 6px; font-weight: 700; font-size: 8.6px; line-height: 10px; text-align: center; }
  .contact-item svg { position: static; }
  .contact-address { left: 0; width: 219px; color: var(--band-text-light); }
  .contact-phone { left: 219px; width: 147px; color: var(--band-text-light); }
  .contact-email { left: 366px; width: 157px; color: var(--band-text-3); }
  .contact-web { left: 523px; width: 141px; color: var(--band-text-4); }
</style>
</head>
<body>
  <main class="letterhead">
    <div class="side-bar"></div>

    <header class="brand">
      <div class="brand-square"></div>
      <span class="brand-name">TWM Norvane</span>
    </header>

    <div class="letter-date">Date, 01 April 2021</div>

    <section class="letter-body">
      <div class="recipient">
        <div>To:</div>
        <div class="recipient-name">Corin Haldane</div>
        <div class="recipient-role">Chief Officer</div>
      </div>
      <p>Lorem ipsum dolor sit amet, consectetur adipiscing elit. Duis auctor sem vel metus interdum porta. Duis consequat bibendum felis eget cursus. Nulla eget purus vehicula ipsum finibus egestas. Nullam ligula ipsum, mollis sed gravida vitae, maximus eu dolor. Morbi luctus sem a congue consectetur.</p>
      <p>Orci varius natoque penatibus et magnis dis parturient montes, nascetur ridiculus mus. Vestibulum congue eros auctor, ullamcorper libero blandit, tempor tellus. Proin vitae tellus et nunc fringilla lacinia. Sed augue erat, facilisis laoreet velit a, convallis mattis nunc. Nunc sagittis ligula vitae sollicitudin sollicitudin.</p>
      <p>Nulla facilisi. Nulla quis odio vitae purus aliquam fermentum ut nec diam. Fusce sed velit ultrices, aliquam augue ut, sollicitudin orci.</p>
    </section>

    <div class="sign-off">Kind Regards</div>
    <div class="signature" role="img" aria-label="Handwritten signature of the sender"></div>
    <div class="sender-name">Corin Haldane</div>

    <footer class="contact-band">
      <svg width="664" height="77" viewBox="0 0 664 77">
        <rect x="0" y="0" width="664" height="77" fill="var(--band-4)"/>
        <polygon points="0,0 505,0 526,38.5 505,77 0,77" fill="var(--band-3)"/>
        <polygon points="0,0 347,0 368,38.5 347,77 0,77" fill="var(--band-2)"/>
        <polygon points="0,0 203,0 223,38.5 203,77 0,77" fill="var(--band-1)"/>
      </svg>

      <div class="contact-item contact-address">
        <svg width="18" height="18" viewBox="0 0 18 18" aria-hidden="true">
          <path d="M9 1C5.7 1 3.2 3.5 3.2 6.7 3.2 11 9 17 9 17s5.8-6 5.8-10.3C14.8 3.5 12.3 1 9 1z" fill="#fff"/>
          <circle cx="9" cy="6.8" r="2.6" fill="var(--band-1)"/>
        </svg>
        <span>4th Floor, 118 Harlow Lane<br>London E2 7QP United Kingdom</span>
      </div>

      <div class="contact-item contact-phone">
        <svg width="18" height="18" viewBox="0 0 18 18" aria-hidden="true">
          <circle cx="9" cy="9" r="9" fill="#fff"/>
          <path d="M6.2 4.4l1.6 2.2-.9 1.2c.6 1.3 1.6 2.3 2.9 2.9l1.2-.9 2.2 1.6-.8 1.8c-3.9-.3-7.1-3.5-7.4-7.4z" fill="var(--band-2)"/>
        </svg>
        <span>+44 (0) 207 555 0192</span>
      </div>

      <div class="contact-item contact-email">
        <svg width="18" height="18" viewBox="0 0 18 18" aria-hidden="true">
          <circle cx="9" cy="9" r="9" fill="#fff"/>
          <rect x="4.5" y="6" width="9" height="6" fill="none" stroke="#8a8a8a" stroke-width="1.1"/>
          <path d="M4.5 6L9 9.6 13.5 6M4.5 12L7.6 8.6M13.5 12l-3.1-3.4" fill="none" stroke="#8a8a8a" stroke-width="1"/>
        </svg>
        <span>info@twm-norvane.com</span>
      </div>

      <div class="contact-item contact-web">
        <svg width="18" height="18" viewBox="0 0 18 18" aria-hidden="true">
          <circle cx="9" cy="9" r="8" fill="none" stroke="#8a8a8a" stroke-width="1.3"/>
          <ellipse cx="9" cy="9" rx="3.5" ry="8" fill="none" stroke="#8a8a8a" stroke-width="1"/>
          <path d="M1.5 6.5h15M1.5 11.5h15" stroke="#8a8a8a" stroke-width="1"/>
        </svg>
        <span>www.twm-norvane.com</span>
      </div>
    </footer>
  </main>
</body>
</html>
```